Creative Business Card

Were looking for a new fresh and creative look to our Business card. Our company name is InkHollow. Be creative, Were attaching our logo and our base colors, but your free to do anything. Name, title, Phone

Industry/Entity Type

Business

```html
<!DOCTYPE html>
<html lang="en">
<head>
<meta charset="utf-8">
<title>InkHollow Business Card</title>
<link rel="stylesheet" href="https://fonts.googleapis.com/css2?family=Source+Sans+3:wght@400;600;700;800&display=swap">
<style>
  :root {
    --backdrop: #adabab;
    --card: #fbfbfb;
    --brand-blue: #0f74bd;
    --brand-green: #7dbb3c;
    --ink: #1e1e1e;
    --ink-soft: #333333;
    --band-dark: #1b1b1b;
    --white: #ffffff;
  }
  * { margin: 0; padding: 0; box-sizing: border-box; }
  html, body {
    width: 1200px; height: 900px; overflow: hidden;
    background: var(--backdrop);
    font-family: "Source Sans 3", "Myriad Pro", Arial, sans-serif;
    color: var(--ink);
  }
  .stage { position: relative; width: 1200px; height: 900px; }

  .side-label {
    position: absolute; width: 200px; text-align: center;
    font-size: 31px; font-weight: 400; color: #222; letter-spacing: 0.5px;
  }
  .side-label--back { left: 270px; top: 238px; }
  .side-label--front { left: 731px; top: 239px; }

  .card {
    position: absolute; width: 442px; border-radius: 14px; overflow: hidden;
    background: var(--card);
  }
  .card svg.card-shapes { position: absolute; inset: 0; }
  .card--back { left: 151px; top: 314px; height: 263px; }
  .card--front { left: 614px; top: 313px; height: 259px; }

  .wordmark {
    position: absolute; font-weight: 800; color: var(--brand-green);
    letter-spacing: 0.5px; line-height: 1; white-space: nowrap;
  }
  .card--back .wordmark { left: 0; width: 442px; text-align: center; top: 106px; font-size: 48px; }
  .card--front .wordmark { left: 248px; width: 180px; text-align: center; top: 189px; font-size: 33px; }

  .holder-name {
    position: absolute; left: 25px; top: 40px;
    font-size: 18px; font-weight: 700; color: var(--brand-blue);
  }
  .holder-title {
    position: absolute; left: 26px; top: 59px; width: 408px;
    display: flex; align-items: flex-end; gap: 3px;
    font-size: 12px; color: var(--ink-soft);
  }
  .holder-title::after {
    content: ""; flex: 1; height: 1px; background: #555; margin-bottom: 3px;
  }

  .contact-list { position: absolute; left: 26px; top: 98px; list-style: none; }
  .contact-item {
    display: flex; align-items: center; gap: 6px;
    height: 17.5px; font-size: 13px; color: var(--ink);
  }
  .contact-icon { width: 12px; height: 12px; flex: none; }

  .address {
    position: absolute; left: 26px; top: 201px;
    font-size: 12.5px; line-height: 16px; color: var(--white);
  }
  .address-line { display: flex; align-items: center; gap: 6px; }
  .address-line--indent { padding-left: 17px; }
  .address svg { width: 11px; height: 12px; }
</style>
</head>
<body>
<main class="stage">
  <div class="side-label side-label--back">BACK</div>
  <div class="side-label side-label--front">FRONT</div>

  <section class="card card--back" aria-label="Card back">
    <svg class="card-shapes" width="442" height="263" viewBox="0 0 442 263">
      <polygon points="18,0 424,0 411,22 31,22" fill="var(--brand-blue)"/>
      <polyline points="20,0 32,26 410,26 422,0" fill="none" stroke="var(--brand-green)" stroke-width="2"/>
      <polygon points="18,263 424,263 411,240 31,240" fill="var(--brand-blue)"/>
      <polyline points="20,263 32,235 410,235 422,263" fill="none" stroke="var(--brand-green)" stroke-width="2"/>
    </svg>
    <div class="wordmark">InkHollow</div>
  </section>

  <section class="card card--front" aria-label="Card front">
    <svg class="card-shapes" width="442" height="259" viewBox="0 0 442 259">
      <polygon points="0,0 198,0 190,12 0,12" fill="var(--brand-blue)"/>
      <polygon points="198,0 442,0 442,12 190,12" fill="var(--brand-green)"/>
      <polygon points="0,197 220,197 190,237 0,237" fill="var(--band-dark)"/>
      <polygon points="248,171 442,171 442,237 198,237" fill="var(--brand-blue)"/>
    </svg>

    <div class="holder-name">Your Name</div>
    <div class="holder-title">Your title</div>

    <ul class="contact-list">
      <li class="contact-item">
        <svg class="contact-icon" viewBox="0 0 12 12"><rect width="12" height="12" rx="2" fill="var(--brand-blue)"/><path d="M3.5 2.5c-.6.4-.9 1-.6 2 .6 2 2.2 3.8 4.3 4.6 1 .3 1.6 0 2-.6l-1.3-1.3-1 .5c-.9-.5-1.6-1.2-2-2.1l.5-1z" fill="var(--white)"/></svg>
        0123 456 789
      </li>
      <li class="contact-item">
        <svg class="contact-icon" viewBox="0 0 12 12"><rect width="12" height="12" rx="2" fill="var(--brand-blue)"/><rect x="4" y="2" width="4" height="8" rx="0.8" fill="none" stroke="var(--white)" stroke-width="1"/></svg>
        0123 456 789
      </li>
      <li class="contact-item">
        <svg class="contact-icon" viewBox="0 0 12 12"><rect width="12" height="12" rx="2" fill="var(--brand-blue)"/><text x="6" y="9" text-anchor="middle" font-size="7.5" font-weight="700" fill="var(--white)" font-family="Source Sans 3, sans-serif">Fx</text></svg>
        0123 456 789
      </li>
      <li class="contact-item">
        <svg class="contact-icon" viewBox="0 0 12 12"><rect width="12" height="12" rx="2" fill="var(--brand-blue)"/><text x="6" y="9" text-anchor="middle" font-size="9" font-weight="700" fill="var(--white)" font-family="Source Sans 3, sans-serif">@</text></svg>
        youremail@mail.com
      </li>
      <li class="contact-item">
        <svg class="contact-icon" viewBox="0 0 12 12"><rect width="12" height="12" rx="2" fill="var(--brand-blue)"/><circle cx="6" cy="6" r="3.6" fill="none" stroke="var(--white)" stroke-width="0.9"/><path d="M2.4 6h7.2M6 2.4c-1.6 2-1.6 5.2 0 7.2M6 2.4c1.6 2 1.6 5.2 0 7.2" fill="none" stroke="var(--white)" stroke-width="0.7"/></svg>
        www.yourwebdite.com
      </li>
    </ul>

    <div class="address">
      <div class="address-line">
        <svg viewBox="0 0 11 12"><rect width="11" height="12" rx="2" fill="var(--white)"/><path d="M5.5 2.2a2.4 2.4 0 0 0-2.4 2.4c0 1.8 2.4 4.6 2.4 4.6s2.4-2.8 2.4-4.6a2.4 2.4 0 0 0-2.4-2.4z" fill="var(--band-dark)"/><circle cx="5.5" cy="4.6" r="0.9" fill="var(--white)"/></svg>
        our address put here
      </div>
      <div class="address-line address-line--indent">your address put here</div>
    </div>

    <div class="wordmark">InkHollow</div>
  </section>
</main>
</body>
</html>
```